Bus Card - T.K. Gate Co
T.K. Gate Co
Project: Bus Card - T.K. Gate Co
Creative Brief
Professional
Owner
4172 Pelton Lane Cedar Hollow, OH 45999
tkmorrowventures@mailpost.example
Would prefer a design for wooden business cards.

```html
<!DOCTYPE html>
<html lang="en">
<head>
<meta charset="utf-8">
<title>Bus Card - T.K. Gate Co</title>
<link rel="stylesheet" href="https://fonts.googleapis.com/css2?family=Playfair+Display:wght@700&family=Roboto:wght@400&display=swap">
<style>
  :root {
    --backdrop: #e4e5e6;
    --forest: #2b4a3c;
    --paper: #ffffff;
    --bark: #8c5a3a;
    --ink: #6a6a6a;
    --muted: #9a9a9a;
    --rule: #cfcfcf;
    --accent: #c9773b;
  }
  * { margin: 0; padding: 0; box-sizing: border-box; }
  html, body { width: 1200px; height: 901px; overflow: hidden; }
  body {
    background: var(--backdrop);
    font-family: "Roboto", sans-serif;
    position: relative;
  }
  .card {
    position: absolute;
    left: 300px;
    width: 600px;
    height: 344px;
    border-radius: 24px;
  }
  .card--front { top: 68px; background: var(--forest); }
  .card--back { top: 486px; background: var(--paper); }

  .front-brand {
    position: absolute;
    inset: 0;
    display: flex;
    align-items: center;
    justify-content: center;
    gap: 18px;
  }
  .brand-mark {
    width: 22px; height: 22px;
    background: var(--paper);
  }
  .front-brand .brand-name {
    font-family: "Playfair Display", serif;
    font-weight: 700;
    font-size: 46px;
    color: var(--paper);
    letter-spacing: 1px;
  }

  .back-brand {
    position: absolute;
    left: 40px; top: 0;
    width: 240px; height: 100%;
    display: flex;
    align-items: center;
    justify-content: center;
  }
  .back-brand .brand-name {
    font-family: "Playfair Display", serif;
    font-weight: 700;
    font-size: 30px;
    color: var(--forest);
  }
  .divider {
    position: absolute;
    left: 298px; top: 70px;
    width: 1px; height: 206px;
    background: var(--rule);
  }
  .details {
    position: absolute;
    left: 320px; top: 74px;
    color: var(--ink);
  }
  .details .company {
    font-family: "Playfair Display", serif;
    font-weight: 700;
    font-size: 27px;
    color: var(--bark);
    line-height: 1;
  }
  .details .role { font-size: 12px; color: var(--muted); margin-top: 4px; }
  .details .address { font-size: 13px; line-height: 1.45; margin-top: 30px; }
  .contact { list-style: none; margin-top: 26px; font-size: 12.5px; line-height: 1.65; }
  .contact li { display: flex; align-items: center; gap: 9px; }
  .contact svg { width: 11px; height: 11px; flex: none; }
</style>
</head>
<body>
  <section class="card card--front">
    <div class="front-brand">
      <span class="brand-mark"></span>
      <span class="brand-name">T.K. Gate Co</span>
    </div>
  </section>

  <section class="card card--back">
    <div class="back-brand">
      <span class="brand-name">T.K. Gate Co</span>
    </div>
    <div class="divider"></div>
    <div class="details">
      <h1 class="company">T.K. GATE CO</h1>
      <p class="role">Owner</p>
      <p class="address">4172 Pelton Lane<br>Cedar Hollow, OH 45999</p>
      <ul class="contact">
        <li><svg viewBox="0 0 12 12"><path d="M2 1l2.5 0 1 3-1.5 1a6 6 0 0 0 3 3l1-1.5 3 1V10a1.5 1.5 0 0 1-1.5 1.5A9 9 0 0 1 .5 2.5 1.5 1.5 0 0 1 2 1z" fill="var(--accent)"/></svg>555-555-0142</li>
        <li><svg viewBox="0 0 12 12"><rect x="3" y="0.5" width="6" height="11" rx="1.2" fill="var(--ink)"/><rect x="4" y="2" width="4" height="7" fill="var(--paper)"/></svg>555-555-0187</li>
        <li><svg viewBox="0 0 12 12"><rect x="0.5" y="2" width="11" height="8" rx="1" fill="var(--bark)"/><path d="M1 2.5l5 4 5-4" stroke="var(--paper)" fill="none"/></svg>tkmorrowventures@mailpost.example</li>
        <li><svg viewBox="0 0 12 12"><circle cx="6" cy="6" r="5.5" fill="var(--accent)"/><path d="M0.5 6h11M6 .5c-3 3-3 8 0 11M6 .5c3 3 3 8 0 11" stroke="var(--paper)" stroke-width="0.8" fill="none"/></svg>tkmorrowventures.example</li>
      </ul>
    </div>
  </section>
</body>
</html>
```